Website Design for The KLV Trust

The KLV Trust will be used to raise awareness, point people in the right direction to get more information on the disease and do fundraising for research to cure Dystonia. It will be coordinated with a Facebook page and Instagram and Twitter. I am finalizing the logo now. This website will need to look and feel of a charity page. Fundraising and information will be coordinated with PWTA (harlowen-relief.org). Another web page that is a good example, though it has much more content than I am looking for is the Walter B Crane Foundation.

Target Market(s)

Anyone interested in helping / contributing to fundraisers and / or looking for information on Dystonia

Number of Pages Required

3 page

Font styles to use
Sans Serif

Colors

Designer to choose colors to be used in the design.

Requirements
Must have
• I would like a large header with the logo and slogan at the top to clearly identify what page you are on, a "click here to donate" button to jump them to the donation page and three areas of information below - What is dystonia, How can I help fight for the cure and a "who is KLV" area. I will also need links to Facebook, Instagram and Twitter to coordinate with KLV Trust pages
Should not have
• This page should be treated like a charity page so it shouldn't have the look or feel of a for profit business or other type of page

```html
<!DOCTYPE html>
<html lang="en">
<head>
<meta charset="utf-8">
<title>The KLV Trust – Fighting for a Cure for Dystonia</title>
<link rel="stylesheet" href="https://fonts.googleapis.com/css2?family=Lato:wght@300;400;700&display=swap">
<style>
:root{
  --red:#d40f15;
  --dark:#333333;
  --text:#444444;
  --muted:#666666;
  --light-bg:#f5f5f5;
  --card-bg:#f3f3f3;
  --white:#ffffff;
  --line:#dddddd;
}
*{box-sizing:border-box;margin:0;padding:0}
html,body{width:1200px;height:3818px;overflow:hidden}
body{position:relative;font-family:'Lato',sans-serif;color:var(--text);background:var(--white)}
.abs{position:absolute}
a{color:inherit;text-decoration:none}

/* top bar */
.topbar{left:0;top:0;width:1200px;height:36px;background:var(--dark);color:#eee;font-size:13px}
.topbar .mail{left:90px;top:10px;display:flex;align-items:center;gap:8px}
.topbar .phone{left:548px;top:10px;display:flex;align-items:center;gap:6px}
.topbar .socials{right:60px;top:0;display:flex;height:36px}
.topbar .socials span{width:36px;height:36px;display:flex;align-items:center;justify-content:center}
.topbar .socials span i{width:11px;height:11px;border-radius:50%;background:#eee;display:block}
.topbar .socials span.active{background:var(--red)}

/* header */
.header{left:0;top:36px;width:1200px;height:143px;background:var(--white)}
.menu-icon{left:88px;top:65px}
.brand{left:520px;top:18px;width:160px;text-align:center}
.brand .mark{width:66px;height:66px;border-radius:50%;background:var(--red);margin:0 auto 8px}
.brand .name{font-size:20px;font-weight:700;color:var(--dark);letter-spacing:.5px}
.btn{display:flex;align-items:center;justify-content:center;background:var(--red);color:var(--white);border-radius:20px;font-size:14px}
.header .btn{left:963px;top:54px;width:163px;height:36px}

/* hero */
.hero{left:0;top:179px;width:1200px;height:528px;background:linear-gradient(120deg,#cfe6f1 0%,#b7d9ea 45%,#d9edf5 100%)}
.hero-arrow{width:32px;height:32px;border-radius:50%;background:rgba(80,80,80,.55);top:270px;display:flex;align-items:center;justify-content:center}
.hero-dots{left:580px;top:460px;display:flex;gap:9px}
.hero-dots i{width:8px;height:8px;border-radius:50%;background:#444;display:block}
.hero-dots i:first-child{background:var(--red)}

/* features */
.features{left:0;top:707px;width:1200px;height:395px;background:var(--light-bg)}
.feature{width:340px;text-align:center}
.feature svg{display:block;margin:0 auto}
.feature h3{font-weight:300;font-size:35px;color:var(--dark);margin-top:20px}
.feature p{font-size:14px;line-height:16px;color:var(--muted);margin-top:20px}
.feature .more{font-size:14px;color:var(--muted);margin-top:20px;display:inline-flex;align-items:center;gap:3px}

/* section headings */
.sec-title{font-weight:300;font-size:38px;color:var(--dark);line-height:1.05}
.sec-rule{width:93px;height:2px;background:var(--red)}
.body-text{font-size:14px;line-height:16px;color:var(--muted)}
.body-text p+p{margin-top:16px}

/* about */
.video-shadow{left:610px;top:1185px;width:498px;height:326px;background:#eeeeee}
.video{left:628px;top:1161px;width:498px;height:331px;background:linear-gradient(180deg,#3f7fc4 0%,#8fb7dd 55%,#a9a39a 75%,#7e7a73 100%)}
.play{left:220px;top:145px;width:58px;height:40px;border-radius:10px;background:var(--red);display:flex;align-items:center;justify-content:center}

/* fundraising */
.fund-photo{left:0;top:1582px;width:607px;height:458px;background:linear-gradient(160deg,#6e7c45 0%,#8c9a5a 40%,#b7a98c 80%,#9b958a 100%)}
.fund-panel{left:607px;top:1582px;width:593px;height:458px;background:var(--light-bg)}

/* news */
.center{left:0;width:1200px;text-align:center}
.news-card{top:2210px;width:335px;height:390px;background:var(--white);box-shadow:0 0 12px rgba(0,0,0,.08);padding:12px 10px 0}
.news-card .img{height:208px}
.news-card .meta{display:flex;justify-content:space-between;font-size:12px;color:var(--muted);padding:10px 6px 6px;border-bottom:1px solid var(--line)}
.news-card .meta span{display:flex;align-items:center;gap:4px}
.news-card h4{font-weight:400;font-size:15px;color:var(--text);margin:14px 6px 6px}
.news-card p{font-size:13.5px;line-height:16px;color:var(--muted);margin:0 6px}
.news-card .cont{font-size:13px;color:var(--muted);margin:14px 6px 0;display:flex;align-items:center;gap:6px}

/* reviews */
.review{top:2726px;width:298px;height:256px;background:var(--card-bg);text-align:center;padding-top:40px}
.review h5{font-weight:300;font-size:20px;color:var(--dark);margin-top:18px}
.review .role{font-size:13px;color:var(--muted);margin-top:5px}
.review p{font-size:12.5px;line-height:15px;color:var(--muted);margin-top:12px;padding:0 30px}
.rev-dots{left:589px;top:3011px;display:flex;gap:6px}
.rev-dots i{width:7px;height:7px;border-radius:50%;background:#aaa;display:block}
.rev-dots i:first-child{background:var(--red)}

/* help + newsletter */
.help{left:84px;top:3205px;width:454px}
.help h2,.news-sign h2{font-size:32px;font-weight:700}
.help h2{color:var(--dark)}
.help .row{display:flex;align-items:center;gap:14px;font-size:15px;color:var(--muted)}
.news-bg{left:609px;top:3147px;width:591px;height:303px;background:var(--red)}
.news-sign{left:671px;top:3205px;width:470px;color:var(--white)}
.news-sign p{font-size:14.5px;line-height:23px;margin-top:10px;letter-spacing:.2px}
.subscribe-field{left:662px;top:3323px;width:464px;height:58px;border-radius:29px;background:var(--white);display:flex;align-items:center;justify-content:space-between;padding:0 14px 0 31px;font-size:14px;color:#555}
.send{width:36px;height:36px;border-radius:50%;background:var(--red);display:flex;align-items:center;justify-content:center}

/* footer */
.footer{left:0;top:3450px;width:1200px;height:298px;background:var(--dark);color:var(--white)}
.foot-logo{left:87px;top:0;width:192px;height:298px;background:var(--white);text-align:center;padding-top:54px}
.foot-logo .mark{width:64px;height:64px;border-radius:50%;background:var(--red);margin:0 auto 10px}
.foot-logo .name{font-size:19px;font-weight:700;color:var(--dark)}
.foot-logo p{font-size:13px;line-height:16px;color:var(--muted);text-align:left;padding:0 22px;margin-top:38px}
.foot-col h6{font-size:19px;font-weight:400}
.foot-col ul{list-style:disc;margin-top:16px;padding-left:16px;font-size:13px;line-height:24px}
.addr{font-size:13px;line-height:24px;margin-top:14px}
.addr div{display:flex;align-items:center;gap:10px}
.addr .ind{padding-left:24px}
.fin{background:#4a4a4a;border:1px solid #666;color:#ddd;font-size:12px;padding:5px 8px}
.bottom{left:0;top:3748px;width:1200px;height:70px;background:var(--white)}
.bottom .copy{left:87px;top:22px;font-size:13px;color:var(--dark)}
.bottom .soc{left:941px;top:14px;display:flex;gap:12px}
.bottom .soc i{width:27px;height:27px;border-radius:50%;background:var(--dark);display:block}
.bottom .soc i:first-child{background:var(--red)}
</style>
</head>
<body>

<!-- top bar -->
<div class="abs topbar">
  <div class="abs mail">
    <svg width="12" height="9" viewBox="0 0 12 9"><rect x=".5" y=".5" width="11" height="8" fill="none" stroke="#eee"/><path d="M.5 .5 6 5l5.5-4.5" fill="none" stroke="#eee"/></svg>
    info@theklvtrust.org
  </div>
  <div class="abs phone">
    <svg width="11" height="11" viewBox="0 0 24 24"><path d="M6.6 10.8a15 15 0 0 0 6.6 6.6l2.2-2.2a1 1 0 0 1 1-.25 11 11 0 0 0 3.6.6 1 1 0 0 1 1 1V20a1 1 0 0 1-1 1A17 17 0 0 1 3 4a1 1 0 0 1 1-1h3.5a1 1 0 0 1 1 1c0 1.25.2 2.45.57 3.57a1 1 0 0 1-.25 1z" fill="#eee"/></svg>
    +1 555 014 2290
  </div>
  <div class="abs socials" aria-label="Social links">
    <span><i></i></span><span class="active"><i></i></span><span><i></i></span><span><i></i></span><span><i></i></span>
  </div>
</div>

<!-- header -->
<div class="abs header">
  <svg class="abs menu-icon" width="26" height="16" viewBox="0 0 26 16"><path d="M0 1h26M0 8h26M0 15h26" stroke="#333" stroke-width="2"/></svg>
  <div class="abs brand">
    <div class="mark"></div>
    <div class="name">THE KLV TRUST</div>
  </div>
  <a class="abs btn" href="#donate">Donate</a>
</div>

<!-- hero -->
<div class="abs hero" role="img" aria-label="Doctor in a white coat holding a tablet that reads Dystonia">
  <div class="abs hero-arrow" style="left:32px"><svg width="10" height="12" viewBox="0 0 10 12"><path d="M7 1 2 6l5 5" fill="none" stroke="#fff" stroke-width="2"/></svg></div>
  <div class="abs hero-arrow" style="left:1144px"><svg width="10" height="12" viewBox="0 0 10 12"><path d="M3 1l5 5-5 5" fill="none" stroke="#fff" stroke-width="2"/></svg></div>
  <div class="abs hero-dots"><i></i><i></i><i></i><i></i></div>
</div>

<!-- features -->
<div class="abs features">
  <div class="abs feature" style="left:85px;top:45px">
    <svg width="90" height="96" viewBox="0 0 90 96" fill="#d40f15">
      <circle cx="45" cy="16" r="12"/><circle cx="22" cy="34" r="10"/><circle cx="68" cy="34" r="10"/>
      <path d="M28 58a17 17 0 0 1 34 0v12H28z"/><path d="M4 70a18 18 0 0 1 30-13v25H4z"/><path d="M56 57a18 18 0 0 1 30 13v12H56z"/><path d="M28 78a17 17 0 0 1 34 0v14H28z"/>
    </svg>
    <h3>Support Groups</h3>
    <p>Lorem Ipsum is simply dummy text of the printing and typesetting industry. Lorem Ipsum has been a the industry's standard dummy text ever since the 1500s,</p>
    <a class="more" href="#">Read More..<svg width="16" height="16" viewBox="0 0 16 16"><circle cx="8" cy="8" r="7" fill="none" stroke="#444" stroke-width="1.3"/><path d="M7 5l3 3-3 3" fill="none" stroke="#444" stroke-width="1.3"/></svg></a>
  </div>
  <div class="abs feature" style="left:445px;top:45px">
    <svg width="100" height="96" viewBox="0 0 100 96" fill="#d40f15">
      <path d="M50 92 10 52A24 24 0 0 1 50 18a24 24 0 0 1 40 34z"/>
      <path d="M28 44l22 22M36 36l22 22M44 30l18 18" stroke="#fff" stroke-width="4" fill="none"/>
    </svg>
    <h3>Get Involved</h3>
    <p>Lorem Ipsum is simply dummy text of the printing and typesetting industry. Lorem Ipsum has been a the industry's standard dummy text ever since the 1500s,</p>
    <a class="more" href="#">Read More..<svg width="16" height="16" viewBox="0 0 16 16"><circle cx="8" cy="8" r="7" fill="none" stroke="#444" stroke-width="1.3"/><path d="M7 5l3 3-3 3" fill="none" stroke="#444" stroke-width="1.3"/></svg></a>
  </div>
  <div class="abs feature" id="donate" style="left:811px;top:45px">
    <svg width="120" height="96" viewBox="0 0 120 96" fill="#d40f15">
      <path d="M80 50 62 32a11 11 0 0 1 18-12 11 11 0 0 1 18 12z"/>
      <path d="M4 62h16l16-10h22a6 6 0 0 1 0 12H44h18l30-12a6 6 0 0 1 6 10L64 84H28L20 92H4z"/>
    </svg>
    <h3>Donate</h3>
    <p>Lorem Ipsum is simply dummy text of the printing and typesetting industry. Lorem Ipsum has been a the industry's standard dummy text ever since the 1500s,</p>
    <a class="more" href="#">Read More..<svg width="16" height="16" viewBox="0 0 16 16"><circle cx="8" cy="8" r="7" fill="none" stroke="#444" stroke-width="1.3"/><path d="M7 5l3 3-3 3" fill="none" stroke="#444" stroke-width="1.3"/></svg></a>
  </div>
</div>

<!-- about -->
<h2 class="abs sec-title" style="left:89px;top:1208px">About us</h2>
<div class="abs sec-rule" style="left:89px;top:1258px"></div>
<div class="abs body-text" style="left:88px;top:1286px;width:505px">
  <p>Lorem Ipsum is simply dummy text of the printing and typesetting industry. Lorem Ipsum has been the industry's standard dummy text ever since the 1500s,</p>
  <p>when an unknown printer took a galley of type and scrambled it to make a type specimen book. It has survived not only five centuries,</p>
</div>
<a class="abs btn" href="#" style="left:89px;top:1404px;width:163px;height:36px">Read More</a>
<div class="abs video-shadow"></div>
<div class="abs video" role="img" aria-label="Video still of an empty wheelchair on a paved path under a blue sky">
  <div class="abs play"><svg width="14" height="16" viewBox="0 0 14 16"><path d="M1 1l12 7-12 7z" fill="#fff"/></svg></div>
</div>

<!-- fundraising -->
<div class="abs fund-photo" role="img" aria-label="Nurse helping an elderly man rise from a wheelchair in a park"></div>
<div class="abs fund-panel"></div>
<h2 class="abs sec-title" style="left:650px;top:1674px;width:520px">Fundraising for research to cure Dystonia.</h2>
<div class="abs sec-rule" style="left:652px;top:1770px"></div>
<div class="abs body-text" style="left:651px;top:1804px;width:498px">
  <p>Lorem Ipsum is simply dummy text of the printing and typesetting industry. Lorem Ipsum has been the industry's standard dummy text ever since the 1500s,</p>
  <p>when an unknown printer took a galley of type and scrambled it to make a type specimen book. It has survived not only five centuries,</p>
</div>
<a class="abs btn" href="#" style="left:652px;top:1923px;width:163px;height:36px">Read More</a>

<!-- news -->
<h2 class="abs sec-title center" style="top:2125px">Dystonia News</h2>
<p class="abs center" style="top:2177px;font-size:14px;color:var(--muted)">Lorem Ipsum is simply dummy &nbsp;the printing and typesetting industry.</p>

<div class="abs news-card" style="left:77px">
  <div class="img" role="img" aria-label="Doctor walking with an elderly man using a cane in a park" style="background:linear-gradient(160deg,#7d9a52,#a8b97a 60%,#c9c3b0)"></div>
  <div class="meta"><span>▦ May 31 , 2019</span><span>◯ 20 &nbsp;♡ 12</span></div>
  <h4>What is Lorem Ipsum?</h4>
  <p>Lorem Ipsum is simply dummy &nbsp;the printing and typesetting industry. Lorem Ipsum has been the in the standard dummy.</p>
  <div class="cont">Continue.. <svg width="15" height="15" viewBox="0 0 16 16"><circle cx="8" cy="8" r="7" fill="none" stroke="#555" stroke-width="1.3"/><path d="M7 5l3 3-3 3" fill="none" stroke="#555" stroke-width="1.3"/></svg></div>
</div>
<div class="abs news-card" style="left:440px">
  <div class="img" role="img" aria-label="Smiling woman in a wheelchair stretching her arms outdoors" style="background:linear-gradient(160deg,#a8603e,#c9a27a 50%,#8aa35c)"></div>
  <div class="meta"><span>▦ May 31 , 2019</span><span>◯ 20 &nbsp;♡ 12</span></div>
  <h4>What is Lorem Ipsum?</h4>
  <p>Lorem Ipsum is simply dummy &nbsp;the printing and typesetting industry. Lorem Ipsum has been the in the standard dummy.</p>
  <div class="cont">Continue.. <svg width="15" height="15" viewBox="0 0 16 16"><circle cx="8" cy="8" r="7" fill="none" stroke="#555" stroke-width="1.3"/><path d="M7 5l3 3-3 3" fill="none" stroke="#555" stroke-width="1.3"/></svg></div>
</div>
<div class="abs news-card" style="left:801px">
  <div class="img" role="img" aria-label="Scientists working with microscopes in a laboratory" style="background:linear-gradient(160deg,#2f5f8f,#7ea9cf 50%,#d7e4ee)"></div>
  <div class="meta"><span>▦ Mar 05 , 2019</span><span>◯ 20 &nbsp;♡ 12</span></div>
  <h4>What is Lorem Ipsum?</h4>
  <p>Lorem Ipsum is simply dummy &nbsp;the printing and typesetting industry. Lorem Ipsum has been the in the standard dummy.</p>
  <div class="cont">Continue.. <svg width="15" height="15" viewBox="0 0 16 16"><circle cx="8" cy="8" r="7" fill="none" stroke="#555" stroke-width="1.3"/><path d="M7 5l3 3-3 3" fill="none" stroke="#555" stroke-width="1.3"/></svg></div>
</div>

<!-- reviews -->
<h2 class="abs sec-title center" style="top:2652px;font-size:34px">Customers Reviews</h2>
<div class="abs review" style="left:104px">
  <svg width="44" height="36" viewBox="0 0 44 36" fill="#555"><path d="M0 36V18C0 8 6 1 17 0v7c-5 1-8 5-8 10h8v19zM26 36V18c0-10 6-17 17-18v7c-5 1-8 5-8 10h8v19z"/></svg>
  <h5>Delia Marsh</h5><div class="role">Creative Director</div>
  <p>Lorem Ipsum is simply dummy text of the printing and typesetting industry. Lorem Ipsum has been the industry's standard dummy</p>
</div>
<div class="abs review" style="left:446px">
  <svg width="44" height="36" viewBox="0 0 44 36" fill="#555"><path d="M0 36V18C0 8 6 1 17 0v7c-5 1-8 5-8 10h8v19zM26 36V18c0-10 6-17 17-18v7c-5 1-8 5-8 10h8v19z"/></svg>
  <h5>Owen Castell</h5><div class="role">Creative Director</div>
  <p>Lorem Ipsum is simply dummy text of the printing and typesetting industry. Lorem Ipsum has been the industry's standard dummy</p>
</div>
<div class="abs review" style="left:791px">
  <svg width="44" height="36" viewBox="0 0 44 36" fill="#555"><path d="M0 36V18C0 8 6 1 17 0v7c-5 1-8 5-8 10h8v19zM26 36V18c0-10 6-17 17-18v7c-5 1-8 5-8 10h8v19z"/></svg>
  <h5>Ruth Ellery</h5><div class="role">Creative Director</div>
  <p>Lorem Ipsum is simply dummy text of the printing and typesetting industry. Lorem Ipsum has been the industry's standard dummy</p>
</div>
<div class="abs rev-dots"><i></i><i></i><i></i></div>
<a class="abs btn" href="#" style="left:517px;top:3055px;width:163px;height:36px">View More</a>

<!-- help -->
<div class="abs help">
  <h2>Need Help?</h2>
  <div class="row" style="margin-top:12px;padding-bottom:12px;border-bottom:1px solid var(--dark)">
    <svg width="14" height="10" viewBox="0 0 14 10"><rect x=".5" y=".5" width="13" height="9" fill="none" stroke="#777"/><path d="M.5 .5 7 6l6.5-5.5" fill="none" stroke="#777"/></svg>:&nbsp; info@theklvtrust.org
  </div>
  <div class="row" style="margin-top:22px">
    <svg width="13" height="13" viewBox="0 0 24 24"><path d="M6.6 10.8a15 15 0 0 0 6.6 6.6l2.2-2.2a1 1 0 0 1 1-.25 11 11 0 0 0 3.6.6 1 1 0 0 1 1 1V20a1 1 0 0 1-1 1A17 17 0 0 1 3 4a1 1 0 0 1 1-1h3.5a1 1 0 0 1 1 1c0 1.25.2 2.45.57 3.57a1 1 0 0 1-.25 1z" fill="none" stroke="#777" stroke-width="1.6"/></svg>:&nbsp; +1 555 014 2290
  </div>
  <div class="row" style="margin-top:6px">
    <svg width="13" height="13" viewBox="0 0 14 14"><circle cx="7" cy="7" r="6" fill="none" stroke="#777"/><path d="M7 3v4h3" fill="none" stroke="#777"/></svg>:&nbsp; Monday - Saturday 9:00 -18:00hrs.
  </div>
</div>
<div class="abs news-bg"></div>
<div class="abs news-sign">
  <h2>Newsletter Signup</h2>
  <p>Please subscribe and receive our latest news, promotions, events, and clinic updates you can't get anywhere else.</p>
</div>
<div class="abs subscribe-field">Enter your email here*
  <span class="send"><svg width="18" height="18" viewBox="0 0 24 24"><path d="M2 12 22 3l-7 19-3-8z" fill="#fff"/><path d="M12 14 22 3" stroke="#d40f15" stroke-width="1.5"/></svg></span>
</div>

<!-- footer -->
<div class="abs footer">
  <div class="abs foot-logo">
    <div class="mark"></div>
    <div class="name">THE KLV TRUST</div>
    <p>Lorem Ipsum is simply and dummy text of the printing and typesetting..⊙</p>
  </div>
  <div class="abs foot-col" style="left:375px;top:56px">
    <h6>Quick Link</h6>
    <ul><li>Home</li><li>What Is Dystonia</li><li>Get Involved</li><li>About Us</li><li>Blogs</li><li>Contacts</li></ul>
  </div>
  <div class="abs foot-col" style="left:581px;top:56px">
    <h6>Company address</h6>
    <div class="addr">
      <div><svg width="12" height="14" viewBox="0 0 12 14"><path d="M6 13S1 8 1 5a5 5 0 0 1 10 0c0 3-5 8-5 8z" fill="none" stroke="#fff"/><circle cx="6" cy="5" r="1.6" fill="#fff"/></svg> 4810 Harlow Lane Suite 210</div>
      <div class="ind">Brookfield, USA</div>
      <div class="ind">Zip Code : 60513</div>
      <div><svg width="12" height="12" viewBox="0 0 24 24"><path d="M6.6 10.8a15 15 0 0 0 6.6 6.6l2.2-2.2a1 1 0 0 1 1-.25 11 11 0 0 0 3.6.6 1 1 0 0 1 1 1V20a1 1 0 0 1-1 1A17 17 0 0 1 3 4a1 1 0 0 1 1-1h3.5a1 1 0 0 1 1 1c0 1.25.2 2.45.57 3.57a1 1 0 0 1-.25 1z" fill="none" stroke="#fff" stroke-width="1.8"/></svg> (555) 014-2290</div>
      <div class="ind">hello@klvtrust-mail.org</div>
    </div>
  </div>
  <div class="abs foot-col" style="left:836px;top:56px">
    <h6>Contact us</h6>
  </div>
  <div class="abs fin" style="left:837px;top:95px;width:90px;height:26px">Name</div>
  <div class="abs fin" style="left:939px;top:95px;width:86px;height:26px">Email</div>
  <div class="abs fin" style="left:1034px;top:95px;width:92px;height:26px">Phone</div>
  <div class="abs fin" style="left:837px;top:135px;width:289px;height:64px">Message</div>
  <a class="abs btn" href="#" style="left:837px;top:211px;width:142px;height:32px;font-size:14px">Subscribe</a>
</div>
<div class="abs bottom">
  <div class="abs copy">CopyRight © 2019 The KLV TRUST. All Right Reserve</div>
  <div class="abs soc" aria-label="Social links"><i></i><i></i><i></i><i></i><i></i></div>
</div>

</body>
</html>
```